Square Business Cards for Our Restaurant / Event Venue

We need square business cards designed for the management team of our event venue and restaurant. On one side of the card should be the the Harbor Lantern 7 logo and URL www.harborlantern7.example. On the other side should be the Ember Logo and URL www.emberhall7.example. All employee details should be on the side with Ember logo. There will be a total of 5 cards to be created with the design.

Clara Bennquist
clara@harborlantern7.example

main 555.418.3072
direct 555.730.2946

4831 West Orchard Lane SE
Washington, DC 90417

Industry/Entity Type

Business

```html
<!DOCTYPE html>
<html lang="en">
<head>
<meta charset="utf-8">
<title>Ember / Harbor Lantern 7 Business Cards</title>
<link rel="stylesheet" href="https://fonts.googleapis.com/css2?family=Roboto:wght@300;400;500&display=swap">
<style>
  :root {
    --backdrop: #e2e2e2;
    --card-white: #f4f4f4;
    --brand-red: #b51f25;
    --ink: #111111;
    --text-grey: #4a4a4a;
    --divider: #c8c8c8;
    --white: #ffffff;
  }
  * { margin: 0; padding: 0; box-sizing: border-box; }
  html, body {
    width: 1200px;
    height: 960px;
    overflow: hidden;
  }
  body {
    position: relative;
    background: var(--backdrop);
    font-family: "Roboto", Arial, sans-serif;
  }
  .card {
    position: absolute;
    width: 600px;
    height: 342px;
  }
  .card-front {
    left: 302px;
    top: 130px;
    background: var(--card-white);
  }
  .card-back {
    left: 299px;
    top: 488px;
    background: var(--brand-red);
  }

  /* Front */
  .brand-name {
    position: absolute;
    left: 0;
    width: 100%;
    top: 62px;
    text-align: center;
    font-size: 88px;
    font-weight: 500;
    color: var(--ink);
    line-height: 1;
    letter-spacing: 1px;
  }
  .person {
    position: absolute;
    right: 342px;
    top: 220px;
    text-align: right;
  }
  .person-name {
    font-size: 21px;
    font-weight: 500;
    color: var(--brand-red);
    text-transform: uppercase;
    line-height: 24px;
  }
  .person-role {
    font-size: 15px;
    font-weight: 500;
    color: var(--ink);
    line-height: 20px;
    margin-bottom: 2px;
  }
  .person-address {
    font-style: normal;
    font-size: 14.5px;
    color: var(--text-grey);
    line-height: 20px;
  }
  .divider {
    position: absolute;
    left: 278px;
    top: 222px;
    width: 1px;
    height: 86px;
    background: var(--divider);
  }
  .contact-list {
    position: absolute;
    left: 298px;
    top: 222px;
    list-style: none;
  }
  .contact-item {
    display: flex;
    align-items: center;
    font-size: 14.5px;
    color: var(--text-grey);
    line-height: 19px;
  }
  .contact-icon {
    width: 12px;
    height: 12px;
    margin-right: 9px;
    fill: var(--brand-red);
    flex: none;
  }

  /* Back */
  .badge {
    position: absolute;
    left: 205px;
    top: 62px;
    width: 190px;
    height: 190px;
    border-radius: 50%;
    background: var(--white);
    display: flex;
    align-items: center;
    justify-content: center;
    text-align: center;
  }
  .badge-name {
    font-size: 28px;
    font-weight: 300;
    color: var(--brand-red);
    line-height: 32px;
  }
  .back-url {
    position: absolute;
    left: 0;
    width: 100%;
    top: 290px;
    text-align: center;
    font-size: 14.5px;
    color: var(--white);
    letter-spacing: 2.6px;
  }
</style>
</head>
<body>

<section class="card card-front">
  <div class="brand-name">Ember</div>

  <div class="person">
    <div class="person-name">Clara Bennquist</div>
    <div class="person-role">CEO/FOUNDER</div>
    <address class="person-address">4831 West Orchard Lane SE<br>Washington, DC 90417</address>
  </div>

  <div class="divider"></div>

  <ul class="contact-list">
    <li class="contact-item">
      <svg class="contact-icon" viewBox="0 0 24 24"><path d="M6.6 10.8c1.4 2.8 3.8 5.1 6.6 6.6l2.2-2.2c.3-.3.7-.4 1-.2 1.1.4 2.3.6 3.6.6.6 0 1 .4 1 1V20c0 .6-.4 1-1 1C10.6 21 3 13.4 3 4c0-.6.4-1 1-1h3.5c.6 0 1 .4 1 1 0 1.3.2 2.5.6 3.6.1.3 0 .7-.2 1L6.6 10.8z"/></svg>
      555.418.3072
    </li>
    <li class="contact-item">
      <svg class="contact-icon" viewBox="0 0 24 24"><path d="M6.6 10.8c1.4 2.8 3.8 5.1 6.6 6.6l2.2-2.2c.3-.3.7-.4 1-.2 1.1.4 2.3.6 3.6.6.6 0 1 .4 1 1V20c0 .6-.4 1-1 1C10.6 21 3 13.4 3 4c0-.6.4-1 1-1h3.5c.6 0 1 .4 1 1 0 1.3.2 2.5.6 3.6.1.3 0 .7-.2 1L6.6 10.8z"/></svg>
      555.730.2946
    </li>
    <li class="contact-item">
      <svg class="contact-icon" viewBox="0 0 24 24"><path d="M2 5h20v14H2z M3 6l9 7 9-7" stroke="#f4f4f4" stroke-width="1.5"/></svg>
      clara@harborlantern7.example
    </li>
    <li class="contact-item">
      <svg class="contact-icon" viewBox="0 0 24 24"><circle cx="12" cy="12" r="10"/><path d="M2 12h20M12 2c3 3 3 17 0 20M12 2c-3 3-3 17 0 20" stroke="#f4f4f4" stroke-width="1.5" fill="none"/></svg>
      www.emberhall7.example
    </li>
  </ul>
</section>

<section class="card card-back">
  <div class="badge">
    <div class="badge-name">Harbor<br>Lantern 7</div>
  </div>
  <div class="back-url">www.harborlantern7.example</div>
</section>

</body>
</html>
```